Client Meeting and installation Email Follow up

I would like a follow-up email template created.
Currently, we do a lot of new construction builds and meet with clients about 6-3 months before they take possession of their new house. I want a follow-up email template to be sent after the homeowner takes possession of their house that enquires if the clients are happy about their new lighting, the service they received, and their customer service representative with Meridale Glow and Breeze. I have attached a few files of what our current marketing looks like.
Target Market(s)
Home Owners We have already met with
Industry/Entity Type
Residential lighting
Font styles to use
Other font styles liked:
- Alta Light, Playfair Display, Montserrat
Colors
Designer to choose colors to be used in the design.
Look and feel
Each slider illustrates characteristics of the customer's brand and the style your logo design should communicate.

```html
<!DOCTYPE html>
<html lang="en">
<head>
<meta charset="utf-8">
<title>Meridale Glow and Breeze – New Home Follow-up</title>
<link rel="stylesheet" href="https://fonts.googleapis.com/css2?family=Montserrat:wght@400;500;600&family=Inter:wght@400&family=Kaushan+Script&display=swap">
<style>
  :root {
    --ink: #000000;
    --paper: #ffffff;
    --body-text: #7a7a7a;
    --footer-band: #f0f0f0;
    --footer-text: #6e6e6e;
    --hero-warm: #c9a98a;
    --hero-light: #eeeeec;
    --hero-floor: #dcdad6;
    --panel-veil: rgba(150, 150, 150, 0.38);
  }
  * { margin: 0; padding: 0; box-sizing: border-box; }
  html, body { width: 800px; height: 1200px; overflow: hidden; background: var(--paper); }
  .email {
    position: relative;
    width: 800px;
    height: 1200px;
    overflow: hidden;
    background: var(--paper);
    font-family: "Montserrat", sans-serif;
  }

  /* Hero */
  .hero {
    position: absolute;
    left: 0; top: 0;
    width: 800px; height: 480px;
    background:
      linear-gradient(90deg, rgba(170,110,70,0.55) 0%, rgba(200,170,140,0.35) 22%, rgba(235,235,232,0) 45%),
      linear-gradient(180deg, var(--hero-light) 0%, #e4e2de 60%, var(--hero-floor) 100%);
  }
  .brand-mark {
    position: absolute;
    background: var(--paper);
    color: var(--ink);
    font-family: "Montserrat", sans-serif;
    font-weight: 500;
    text-align: center;
    text-transform: uppercase;
    line-height: 1.05;
  }
  .hero .brand-mark {
    left: 94px; top: 23px;
    width: 312px; height: 91px;
    padding-top: 14px;
    font-size: 27px;
    letter-spacing: 1px;
  }
  .hero-panel {
    position: absolute;
    left: 96px; top: 137px;
    width: 622px; height: 285px;
    border-radius: 14px;
    background: var(--panel-veil);
  }
  .hero-title {
    position: absolute;
    left: 96px; top: 148px;
    width: 622px;
    text-align: center;
    color: var(--paper);
    font-family: "Kaushan Script", cursive;
    font-weight: 400;
    font-size: 58px;
    line-height: 88px;
    letter-spacing: 2px;
    text-shadow: 2px 3px 4px rgba(0,0,0,0.35);
  }

  /* Letter */
  .letter {
    position: absolute;
    left: 38px; top: 509px;
    width: 730px;
    color: var(--body-text);
    font-size: 16.5px;
    line-height: 27.5px;
  }
  .letter p { margin-bottom: 27.5px; }

  /* Footer */
  .signature-band {
    position: absolute;
    left: 0; top: 963px;
    width: 800px; height: 199px;
    background: var(--footer-band);
  }
  .signature-band .brand-mark {
    left: 40px; top: 51px;
    width: 335px; height: 99px;
    padding-top: 17px;
    font-size: 29px;
    letter-spacing: 1px;
  }
  .rep {
    position: absolute;
    left: 425px; top: 14px;
    font-family: "Inter", sans-serif;
    color: var(--footer-text);
    font-size: 14.5px;
  }
  .rep-name {
    font-family: "Kaushan Script", cursive;
    font-size: 34px;
    color: var(--ink);
    line-height: 46px;
    margin-bottom: 4px;
  }
  .rep-line { line-height: 31.5px; }
  .social-row {
    display: flex;
    gap: 26px;
    margin-top: 8px;
    margin-left: 9px;
  }
  .social-dot {
    width: 31px; height: 31px;
    border-radius: 50%;
    background: var(--ink);
  }
  .copyright {
    position: absolute;
    left: 0; top: 1170px;
    width: 800px;
    text-align: center;
    font-family: "Inter", sans-serif;
    color: #9a9a9a;
    font-size: 14px;
  }
</style>
</head>
<body>
<main class="email">
  <header class="hero" role="img" aria-label="Photo of a bright, modern living and dining room with a leather lounge chair, wooden table and tall windows">
    <div class="brand-mark">Meridale<br>Glow &amp; Breeze</div>
    <div class="hero-panel"></div>
    <h1 class="hero-title">We Hope You’re<br>Enjoying<br>Your New Home!</h1>
  </header>

  <section class="letter">
    <p>Dear [Homeowner's Name],</p>
    <p>&nbsp;Congratulations on your new home! We are thrilled to have been a part of your journey and hope that you are settling in nicely.</p>
    <p>We wanted to take a moment to check in and see how you're enjoying your new lighting. Your satisfaction is our top priority, and we'd love to know if the lighting design meets your expectations.</p>
    <p>Additionally, we would appreciate your feedback on the service you received from our team. Was there anything we could have done better? Your insights are invaluable to us as we strive to continuously improve.</p>
    <p>Thank you for choosing Meridale Glow and Breeze. We look forward to hearing from you!</p>
  </section>

  <footer class="signature-band">
    <div class="brand-mark">Meridale<br>Glow &amp; Breeze</div>
    <div class="rep">
      <div class="rep-name">Elena Marsh</div>
      <div class="rep-line">Customer Service Representative</div>
      <div class="rep-line">Cell: 403.555.0187</div>
      <div class="rep-line">1820 Larkspur Road S.E, Calgary, AB T2G 0X4 CA</div>
      <div class="social-row">
        <span class="social-dot" aria-label="Social profile link"></span>
        <span class="social-dot" aria-label="Social profile link"></span>
        <span class="social-dot" aria-label="Social profile link"></span>
        <span class="social-dot" aria-label="Social profile link"></span>
        <span class="social-dot" aria-label="Social profile link"></span>
      </div>
    </div>
  </footer>

  <p class="copyright">© 2024 Meridale Glow &amp; Breeze. All rights reserved.</p>
</main>
</body>
</html>
```